BRVL web site redesign

Coastal Linkwork Systems service (BRVL) is a diverse technology company specialising in design and installation of fibre optics, network convergence and building services, for commercial clients in Australia, we required a new design of our website to attract new clients, generate sales leads, and provide information about our services to the market. The site and should have a new technology look and feel and be designed in word press. our branding colour is blue.

Target Market(s)

New developments, Construction organisations, Commercial end users, IT managers, Consultants.

Industry/Entity Type

It Company

Number of Pages Required

5+ page

Font styles to use
Sans Serif

Colors
0292cd
3176b5

Requirements
Must have
• key pages.
• Home page with some sizzle, automated pictures running through, I like the look of this competitor website http://www.tarelmesh.com.au/ good clean menus and easy to navigate.
• Services page our key services are Fibre optics, Security, Building services,Electrical. I would like the same page layout (Design) for all our services, with a find out more link on each page, manly picture driven with text around our key messaging.
• About us page with space for company profile and directors pictures, bio and contact information.
• Certifications / Accreditations page with have over 20 certifications on different products from suppliers, and a number of licences from governing bodies.
• Current and past projects page with case studies and customer outcomes
• Contact us page with options around what services they require more information on, please keep in mind the site is around generating sales Leeds and being seen as an industry expert.
Nice to have
• RSS feeds, Linked in link, to be placed within the design, Consistent BRVL branding,Same colour blue as our logo Document library for education information, white papers, presentations etc,
• a new technology look and feel, mobile friendly.
Should not have
• boring layout, move away from our cuurent website http://www.brvlgroup.com.au/
• no e eCommerce store required.

```html
<!DOCTYPE html>
<html lang="en">
<head>
<meta charset="utf-8">
<title>BRVL | Coastal Linkwork Systems service</title>
<link href="https://fonts.googleapis.com/css2?family=Arimo:wght@400;700&display=swap" rel="stylesheet">
<style>
:root{
  --brand:#0292cd;
  --brand-deep:#3176b5;
  --ink:#444;
  --muted:#8a8a8a;
  --faint:#b5b5b5;
  --rule:#dedede;
  --black:#000;
  --white:#fff;
  --footer:#f2f0f0;
}
*{margin:0;padding:0;box-sizing:border-box}
html,body{width:953px;height:1200px;overflow:hidden;background:var(--white)}
body{font-family:"Arimo",Arial,sans-serif;color:var(--ink);position:relative}
.wrap{position:absolute;left:214px;width:516px}

/* header */
.site-header{position:absolute;top:0;left:0;width:953px;height:97px}
.brand{position:absolute;left:214px;top:16px;display:flex;align-items:center;gap:10px}
.brand-square{width:30px;height:30px;background:var(--brand)}
.brand-name{font-size:38px;font-weight:700;color:var(--brand);letter-spacing:1px;line-height:1}
.contact-box{position:absolute;left:624px;top:9px;width:110px;white-space:nowrap}
.phone{display:flex;align-items:center;gap:6px;font-size:15px;line-height:18px;color:var(--faint)}
.address{font-size:5.5px;line-height:8.5px;color:var(--faint);margin-top:3px;margin-left:17px}
.main-nav{position:absolute;left:214px;top:75px;width:516px;height:22px;border-top:1px solid var(--rule);display:flex;gap:0}
.main-nav a{font-size:7px;color:var(--muted);text-decoration:none;padding-top:8px;margin-right:30px;position:relative;text-transform:uppercase}
.main-nav a.current{color:var(--brand)}
.main-nav a.current::before{content:"";position:absolute;left:0;right:0;top:-1px;height:2px;background:var(--brand)}
.main-nav a:nth-child(4){margin-right:22px}
.main-nav a:nth-child(5){margin-right:38px}

/* hero */
.hero{position:absolute;top:97px;left:0;width:953px;height:219px;background:var(--black)}
.hero-visual{position:absolute;left:130px;top:0;width:410px;height:219px;
  background:radial-gradient(ellipse at 40% 30%,#39b6e3 0%,#0f6b92 35%,#062a3d 65%,#000 90%)}
.hero-copy{position:absolute;left:533px;top:58px;color:var(--white);font-size:14px;line-height:19px;text-align:right;width:175px}
.hero-copy .accent{color:var(--brand);font-size:11px}
.hero-copy .lead{color:var(--brand);font-size:15px}
.hero-dots{position:absolute;left:687px;top:290px;display:flex;gap:3px}
.hero-dots span{width:8px;height:8px;border:1.5px solid var(--white);border-radius:50%}
.hero-dots span.on{border-color:var(--brand)}

/* welcome */
.welcome{top:343px;text-align:center}
.section-title{font-size:15px;font-weight:400;color:#666;letter-spacing:.5px}
.welcome p{font-size:6.3px;line-height:9.6px;color:var(--muted);margin:10px 4px 0}
.welcome hr{border:0;border-top:1px solid var(--rule);width:230px;margin:18px auto 0}

.services{top:450px;display:flex;justify-content:space-between}
.service{width:120px;display:flex;gap:8px}
.service-icon{flex:none;width:22px;height:22px;border-radius:50%;background:#f1f6fa;display:flex;align-items:center;justify-content:center}
.service h3{font-size:6.5px;font-weight:700;color:#555;line-height:8px;margin-top:3px}
.service p{font-size:6px;color:var(--muted);line-height:9px;margin-top:16px}

/* about */
.about-band{position:absolute;top:534px;left:0;width:953px;height:120px;
  background:linear-gradient(90deg,#ececec 0%,#f6f6f6 40%,#e6e6e6 60%,#f3f3f3 100%);text-align:center}
.about-band .section-title{position:absolute;top:22px;left:0;right:0;font-size:13px}
.about-band .title-rule{position:absolute;top:42px;left:446px;width:60px;border-top:1px solid #ccc}
.about-band p{position:absolute;top:52px;left:272px;width:410px;font-size:6.2px;line-height:9.6px;color:#666}
.more-link{font-size:5.5px;color:#666;text-decoration:underline;text-transform:uppercase}
.about-band .more-link{position:absolute;top:86px;left:0;right:0}

/* network systems */
.network{position:absolute;top:654px;left:0;width:953px;height:270px;background:var(--black);text-align:center}
.network .section-title{position:absolute;top:33px;left:0;right:0;color:var(--white);font-size:12.5px}
.network .sub{position:absolute;top:50px;left:0;right:0;font-size:6px;color:#888}
.network .title-rule{position:absolute;top:66px;left:416px;width:120px;border-top:1px solid #333}
.cards{position:absolute;top:95px;left:214px;width:516px;display:flex;justify-content:space-between}
.card{width:120px;height:147px;background:var(--white)}
.card-photo{height:56px;background:linear-gradient(160deg,#7fb1dc 0%,#3d85c3 55%,#255f96 100%)}
.card h4{font-size:7.5px;font-weight:400;color:#555;margin-top:14px}
.card .card-rule{width:30px;border-top:1px solid var(--rule);margin:4px auto 0}
.card p{font-size:6px;line-height:9.4px;color:#666;margin:6px 10px 0}
.card .more-link{display:block;margin-top:10px}

/* news */
.news{position:absolute;top:948px;left:0;width:953px;text-align:center}
.news .section-title{font-size:12.5px}
.news .title-rule{width:40px;border-top:1px solid var(--rule);margin:6px auto 0}
.news-list{position:absolute;top:48px;left:214px;width:516px;display:flex;justify-content:space-between;text-align:left}
.news-item{width:240px;display:flex;gap:10px}
.news-date{flex:none;width:36px;height:36px;border-radius:50%;background:var(--brand-deep);color:var(--white);text-align:center;font-size:10px;line-height:10px;padding-top:8px}
.news-date small{display:block;font-size:7px}
.news-item h5{font-size:7.5px;font-weight:400;color:#555;text-transform:uppercase}
.news-item p{font-size:6px;line-height:9px;color:#666;margin-top:4px}
.news-item .more-link{display:block;margin-top:7px}

.call-line{position:absolute;top:1087px;left:214px;width:516px;border-top:1px solid var(--rule);text-align:center;font-size:9.5px;color:#999;padding-top:6px}

/* footer */
.site-footer{position:absolute;top:1114px;left:0;width:953px;height:86px;background:var(--footer);text-align:center}
.footer-nav{position:absolute;top:22px;left:0;right:0;font-size:6px;color:#777}
.footer-nav a{color:#777;text-decoration:none}
.social{position:absolute;top:39px;left:0;right:0;display:flex;justify-content:center;gap:8px}
.social span{width:15px;height:15px;border-radius:50%;background:#a8a8a8}
.social span.feed{background:var(--brand-deep)}
.copyright{position:absolute;top:61px;left:0;right:0;font-size:5px;color:#999}
</style>
</head>
<body>

<header class="site-header">
  <div class="brand"><span class="brand-square"></span><span class="brand-name">BRVL</span></div>
  <div class="contact-box">
    <div class="phone">
      <svg width="11" height="11" viewBox="0 0 24 24" aria-hidden="true"><path fill="#c4c4c4" d="M6.6 10.8a15.5 15.5 0 0 0 6.6 6.6l2.2-2.2a1 1 0 0 1 1-.25 11.4 11.4 0 0 0 3.6.57 1 1 0 0 1 1 1V20a1 1 0 0 1-1 1A17 17 0 0 1 3 4a1 1 0 0 1 1-1h3.5a1 1 0 0 1 1 1c0 1.25.2 2.45.57 3.57a1 1 0 0 1-.25 1z"/></svg>
      1300 555 214
    </div>
    <div class="address">Suite 8, 41 Harlow Street<br>Brenton Hills NSW 2169<br>PO Box 5520 NSW 2169<br>Telephone 1300 555 214</div>
  </div>
  <nav class="main-nav">
    <a class="current" href="#">Home</a><a href="#">About Us</a><a href="#">Services</a><a href="#">IPS</a><a href="#">Recent Projects</a><a href="#">Blogs</a><a href="#">Contact Us</a>
  </nav>
</header>

<section class="hero">
  <div class="hero-visual" role="img" aria-label="Photograph of glowing blue fibre optic strands"></div>
  <p class="hero-copy">
    <span class="lead">BRVL</span> <span class="accent">has an</span><br>
    Exceptional Team<br>
    <span class="accent">of very</span> Experienced <span class="accent">and</span><br>
    well-qualified management<br>
    <span class="accent">and</span> Tradespersons
  </p>
</section>
<div class="hero-dots"><span class="on"></span><span></span><span></span><span></span></div>

<section class="wrap welcome">
  <h2 class="section-title">WELCOME!</h2>
  <p>BRVL is diversified technology company 100% Australian owned and operated, we provide Communication, Electrical, Security &amp; ICT services for residential and commercial customers. With over 100 years of combined industry knowledge we pride ourselves on innovated solutions that utilises technology advancements which delivers on our customer's expectations.</p>
  <hr>
</section>

<section class="wrap services">
  <div class="service">
    <div class="service-icon"><svg width="12" height="12" viewBox="0 0 12 12" aria-hidden="true"><rect x="1" y="4" width="10" height="7" fill="#3b8fd0"/><rect x="4" y="2" width="4" height="2" fill="none" stroke="#3b8fd0"/></svg></div>
    <div><h3>Commercial Security Systems</h3><p>Ut tortor elit, ullamcorper non odio sollicitudin, fermentum tristique nunc.</p></div>
  </div>
  <div class="service">
    <div class="service-icon"><svg width="12" height="12" viewBox="0 0 12 12" aria-hidden="true"><rect x="4.5" y="1" width="3" height="3" fill="#3b8fd0"/><rect x="0.5" y="8" width="3" height="3" fill="#3b8fd0"/><rect x="4.5" y="8" width="3" height="3" fill="#3b8fd0"/><rect x="8.5" y="8" width="3" height="3" fill="#3b8fd0"/><path d="M6 4v2M2 8V6h8v2M6 6v2" stroke="#3b8fd0" fill="none"/></svg></div>
    <div><h3>Data &amp; Fibre Installations</h3><p>Ut tortor elit, ullamcorper non odio sollicitudin, fermentum tristique nunc.</p></div>
  </div>
  <div class="service">
    <div class="service-icon"><svg width="12" height="12" viewBox="0 0 12 12" aria-hidden="true"><circle cx="4" cy="3" r="2" fill="#3b8fd0"/><rect x="1" y="6" width="6" height="5" fill="#3b8fd0"/><circle cx="9" cy="5" r="1.5" fill="#3b8fd0"/><rect x="7.5" y="7.5" width="3.5" height="3.5" fill="#3b8fd0"/></svg></div>
    <div><h3>Information Communication &amp; Technology</h3><p>Ut tortor elit, ullamcorper non odio sollicitudin, fermentum tristique nunc.</p></div>
  </div>
  <div class="service">
    <div class="service-icon"><svg width="12" height="12" viewBox="0 0 12 12" aria-hidden="true"><circle cx="4.5" cy="7" r="3" fill="none" stroke="#3b8fd0" stroke-width="1.5"/><circle cx="9" cy="3" r="2" fill="none" stroke="#3b8fd0"/></svg></div>
    <div><h3>Electrical Fit Outs</h3><p>Ut tortor elit, ullamcorper non odio sollicitudin, fermentum tristique nunc.</p></div>
  </div>
</section>

<section class="about-band" role="img" aria-label="Faint grey photograph of a network cable connection behind the about section">
  <h2 class="section-title">ABOUT US</h2>
  <div class="title-rule"></div>
  <p>BRVL is a Communications Integration Company incorporating the expertise of Data and Fibre Optic Communications, ICT and low voltage systems, Security and Application Services, with over five decades of experience and successes in their respected field of expertise.</p>
  <a class="more-link" href="#">Read more</a>
</section>

<section class="network">
  <h2 class="section-title">NETWORK SYSTEMS</h2>
  <p class="sub">Ipsum dolor sit amet, consectetur adipiscing elit. Nulla blandit enim ut leo porta porta</p>
  <div class="title-rule"></div>
  <div class="cards">
    <article class="card"><div class="card-photo" role="img" aria-label="Blue toned photo of a server room"></div><h4>Harbour Quay Tower</h4><div class="card-rule"></div><p>Harbour Quay occupies nearly six hectares of the southern Brenton CBD, defining</p><a class="more-link" href="#">More</a></article>
    <article class="card"><div class="card-photo" role="img" aria-label="Blue toned photo of patched network cabling"></div><h4>Marden Rise</h4><div class="card-rule"></div><p>Harbour Quay occupies nearly six hectares of the southern Brenton CBD, defining</p><a class="more-link" href="#">More</a></article>
    <article class="card"><div class="card-photo" role="img" aria-label="Blue toned image of a connected globe"></div><h4>Telecommunications</h4><div class="card-rule"></div><p>Harbour Quay occupies nearly six hectares of the southern Brenton CBD, defining</p><a class="more-link" href="#">More</a></article>
    <article class="card"><div class="card-photo" role="img" aria-label="Blue toned photo of server racks"></div><h4>Harbour Quay Tower</h4><div class="card-rule"></div><p>Harbour Quay occupies nearly six hectares of the southern Brenton CBD, defining</p><a class="more-link" href="#">More</a></article>
  </div>
</section>

<section class="news">
  <h2 class="section-title">LATEST NEWS</h2>
  <div class="title-rule"></div>
  <div class="news-list">
    <article class="news-item"><div class="news-date">25<small>JAN</small></div><div><h5>Etiam a odio nec mi</h5><p>Lorem ipsum dolor sit amet, consectetur adipiscing elit. Quisque cursus, sem eget sagittis sagittis, nisl magna sodales eros, ut feugiat velit velit</p><a class="more-link" href="#">Read more</a></div></article>
    <article class="news-item"><div class="news-date">25<small>JAN</small></div><div><h5>Etiam a odio nec mi</h5><p>Lorem ipsum dolor sit amet, consectetur adipiscing elit. Quisque cursus, sem eget sagittis sagittis, nisl magna sodales eros, ut feugiat velit velit</p><a class="more-link" href="#">Read more</a></div></article>
  </div>
</section>

<p class="call-line">Please Call Us Now On 1300 555 214 To Discuss Your Future Options</p>

<footer class="site-footer">
  <nav class="footer-nav"><a href="#">About Us</a> &nbsp;|&nbsp; <a href="#">Services</a> &nbsp;|&nbsp; <a href="#">ISP</a> &nbsp;|&nbsp; <a href="#">Recent Projects</a> &nbsp;|&nbsp; <a href="#">Contact Us</a> &nbsp;|&nbsp; <a href="#">Blog</a></nav>
  <div class="social"><span></span><span></span><span></span><span class="feed"></span></div>
  <p class="copyright">Copyright 2015 BRVL Group. All Rights Reserved.</p>
</footer>

</body>
</html>
```